Stationery Design Project

Would like to have the design elements we created in for our website (www.brook-holdings.example), incorporated in a stationery design layout.
Updates
Colors used in the logo attachments do not need to be used. We are open to different color variations. Looking for a crisp, clean, modern update using the design elements in attachments and which can also be viewed on or website.
A note to designers:
Project Deadline Extended
Reason: Due to update in our project description and requirements, we have decided to extend the deadline of this project to provide ample opportunity to all designers participating .
Requirements
Must have
- Must have continuity with the theme and design features used in our website. Have attached .jpg images of some of the design elements.

```html
<!DOCTYPE html>
<html lang="en">
<head>
<meta charset="utf-8">
<title>Brook Holdings Letterhead</title>
<link rel="stylesheet" href="https://fonts.googleapis.com/css2?family=Jost:wght@400;500;600&display=swap">
<style>
  :root {
    --brand-blue: #0a9be0;
    --brand-green: #3fb54a;
    --name-blue: #1a7cc1;
    --text-gray: #6d6e71;
    --footer-gray: #939598;
    --url-gray: #b9babc;
    --paper: #ffffff;
    --backdrop: #ffffff;
  }
  * { margin: 0; padding: 0; box-sizing: border-box; }
  html, body { width: 943px; height: 1200px; overflow: hidden; background: var(--backdrop); }
  body { font-family: "Jost", sans-serif; }
  .letterhead { position: relative; width: 943px; height: 1200px; background: var(--paper); }
  .top-band { position: absolute; top: 0; left: 0; width: 100%; height: 21px; background: var(--brand-blue); }
  .top-band__accent { position: absolute; top: 0; left: 0; width: 57px; height: 21px; background: var(--brand-green); }
  .brand-name {
    position: absolute; left: 59px; top: 78px;
    font-size: 34px; font-weight: 500; color: var(--name-blue); letter-spacing: -0.3px;
  }
  .address-block {
    position: absolute; left: 516px; top: 74px;
    font-size: 12.5px; line-height: 18.5px; color: var(--text-gray);
  }
  .address-block strong { font-weight: 600; }
  .contact-divider { position: absolute; left: 710px; top: 76px; width: 1px; height: 50px; background: var(--brand-green); }
  .contact-block {
    position: absolute; left: 725px; top: 74px;
    font-size: 12.5px; line-height: 18.5px; color: var(--text-gray); list-style: none;
  }
  .contact-block .label { display: inline-block; width: 24px; color: var(--brand-blue); }
  .watermark-area {
    position: absolute; left: 113px; top: 423px; width: 712px; height: 358px;
    background: radial-gradient(ellipse at center, #f4f4f4 0%, #fafafa 55%, rgba(255,255,255,0) 75%);
  }
  .website {
    position: absolute; left: 0; width: 100%; top: 1140px; text-align: center;
    font-size: 22px; color: var(--url-gray); letter-spacing: 0.3px;
  }
  .bottom-band { position: absolute; left: 0; bottom: 0; width: 100%; height: 29px; background: var(--footer-gray); }
</style>
</head>
<body>
  <main class="letterhead">
    <div class="top-band"><div class="top-band__accent"></div></div>

    <div class="brand-name">Brook Holdings</div>

    <address class="address-block" style="font-style: normal;">
      <strong>Brook Holdings, Inc.</strong><br>
      418 Alder Creek Road Suite 120<br>
      Millbrook, GA 30999
    </address>

    <div class="contact-divider"></div>

    <ul class="contact-block">
      <li><span class="label">[P]</span>(555) 201-4830</li>
      <li><span class="label">[F]</span>(555) 201-4831</li>
      <li><span class="label">[E]</span>info@brook-holdings.example</li>
    </ul>

    <div class="watermark-area" role="img" aria-label="Faint large brand mark watermark"></div>

    <div class="website">www.brook-holdings.example</div>
    <div class="bottom-band"></div>
  </main>
</body>
</html>
```